Flyer for The Quiet Bloom Gathering

I am launching my new offering in my business at an event next Sunday where I have a booth and need a flyer advertising the offering, so the flyer needs to stand out for other practitioners that will also be there on the day offering there services.
This flyer is also what I will use for marketing on social media as well as on the day of the event. See the link below to the offering
http://sarahlindqvist.com.au/quiet-bloom-gathering/

Target Market(s)

Women with body image issues - age range 25 - 65
Women with issues around food such as binge eating, emotional eating, eating disorders.

Industry/Entity Type

Health And Wellness

Font styles to use
Serif
Sans Serif
Script

Colors
f9d9e8
85cae6
cee9f5
fee18a
ffffff
eea4c8

Requirements
Must have
• Colours matching my overall website at sarahlindqvist.com.au - pinks, light blue, gold, white
• Imagery similiar to my Instagram, see below https://www.instagram.com/riverstonecarexy/
• - soft, warm, welcoming, nurturing, safe, inviting - see image on sales page for inspiration
• contact details
Should not have
• harsh dark colours or harsh lines

```html
<!DOCTYPE html>
<html lang="en">
<head>
<meta charset="utf-8">
<title>The Quiet Bloom Gathering – Flyer</title>
<link rel="stylesheet" href="https://fonts.googleapis.com/css2?family=Lato:wght@300;400;700&family=Pinyon+Script&display=swap">
<style>
  :root{
    --pink:#eea4c8;
    --pink-soft:#f9d9e8;
    --pink-pale:#fce8f1;
    --blue:#85cae6;
    --blue-soft:#cee9f5;
    --gold:#fee18a;
    --white:#ffffff;
    --ink:#2a2a2a;
    --ink-soft:#5e5e5e;
    --logo:#d64f8a;
  }
  *{box-sizing:border-box;margin:0;padding:0}
  html,body{width:1041px;height:1200px;overflow:hidden;background:#f3f1f4}
  body{font-family:'Lato',sans-serif;color:var(--ink)}
  .flyer{position:relative;width:1041px;height:1200px;background:var(--white);overflow:hidden}
  .abs{position:absolute}

  .header-pink{left:0;top:0;width:554px;height:150px;background:var(--pink-soft)}
  .header-blue{left:554px;top:0;width:487px;height:120px;background:var(--blue)}
  .brand{left:31px;top:28px;font-size:46px;font-weight:300;color:var(--logo);letter-spacing:1px}
  .tagline{left:100px;top:90px;font-size:12px;font-weight:700;color:#3aa7cf}
  .site-url{left:612px;top:20px;font-size:25px;font-weight:300;color:var(--white)}
  .site-url b{font-weight:400;color:#3d3d3d}

  .hero-photo{left:0;top:70px;width:1041px;height:560px;
    background:linear-gradient(180deg,#c9d3e0 0%,#f5d3c8 35%,#fbe2c6 55%,#b8c7cf 75%,#8fa3ad 100%)}
  .hero-veil{left:0;top:70px;width:1041px;height:560px;
    background:linear-gradient(90deg,rgba(252,232,241,.92) 0%,rgba(252,232,241,.8) 48%,rgba(252,232,241,0) 72%)}
  .hero-figure{left:620px;top:105px;width:330px;height:520px;border-radius:160px 160px 30px 30px;
    background:radial-gradient(ellipse at 50% 45%,rgba(110,85,80,.55),rgba(110,85,80,0) 70%)}

  .title{left:51px;top:203px;font-size:38px;font-weight:400;color:var(--ink);line-height:46px}
  .title-rule{left:51px;top:253px;width:430px;height:2px;background:#555}
  .lead{left:51px;top:262px;font-size:23px;font-weight:400;color:#333;line-height:31px}
  .intro{left:51px;width:517px;font-size:13px;font-weight:300;color:var(--ink-soft);line-height:19px;text-align:justify}

  .swoosh{left:0;top:0}

  .right-panel{left:554px;top:600px;width:487px;height:553px;background:var(--pink-pale)}

  .questions{left:36px;top:612px;font-size:16px;font-weight:700;color:var(--ink);line-height:26px}
  .questions .big{font-size:17px}
  .invite{left:36px;top:732px;width:500px;font-size:16.5px;font-weight:300;color:var(--ink-soft);line-height:21px;text-align:justify}

  .receive-band{left:0;top:852px;width:572px;height:54px;background:var(--pink);color:var(--white);
    font-size:19px;font-weight:300;line-height:24px;padding:3px 0 0 36px;text-transform:uppercase}
  .benefits{left:36px;top:926px;width:500px;list-style:none}
  .benefits li{position:relative;padding-left:26px;font-size:16px;font-weight:300;color:var(--ink-soft);line-height:20px;margin-bottom:10px}
  .benefits li.gap{margin-bottom:34px}
  .benefits li.narrow{width:460px}
  .benefits svg{position:absolute;left:0;top:3px}

  .portrait{left:576px;top:666px;width:195px;height:136px;border-radius:22px;
    background:linear-gradient(135deg,#e9d6cf 0%,#e6a0b5 55%,#d9437a 100%)}
  .coach-name{left:578px;top:811px;font-size:21px;font-weight:300;color:#333}
  .quote-mark{font-weight:700;font-size:40px;color:#222;line-height:1}
  .quote{left:811px;top:733px;width:204px;font-size:15px;font-weight:300;color:var(--ink-soft);line-height:19px;text-align:justify}
  .quote-tail{left:595px;top:870px;width:440px;font-size:15px;font-weight:300;color:var(--ink-soft);line-height:19px}
  .investment{left:584px;top:950px;width:431px;font-size:15.5px;font-weight:300;color:var(--ink-soft);line-height:19px;text-align:justify}
  .ready{left:592px;top:1046px;font-family:'Pinyon Script',cursive;font-size:50px;color:#222}
  .social{left:872px;top:1118px;display:flex;gap:8px}
  .social span{display:block;width:26px;height:26px;border:2px solid #333;border-radius:50%}

  .call{left:54px;top:1154px;font-size:34px;font-weight:400;color:#222}
  .call b{font-weight:700;margin-left:12px}
  .email{left:592px;top:1164px;font-size:21px;font-weight:400;color:#222;display:flex;align-items:center;gap:8px}
</style>
</head>
<body>
<main class="flyer">
  <div class="abs hero-photo" role="img" aria-label="Woman stretching her arms to the sky on a beach at sunset"></div>
  <div class="abs hero-figure" aria-hidden="true"></div>
  <div class="abs hero-veil"></div>

  <div class="abs header-pink"></div>
  <div class="abs header-blue"></div>

  <svg class="abs swoosh" width="1041" height="1200" viewBox="0 0 1041 1200" aria-hidden="true">
    <path d="M0 150 L554 150 L554 0 L0 0 Z" fill="#f9d9e8"/>
    <path d="M0 160 C180 190 330 150 520 100 C700 55 880 60 1041 105 L1041 70 C880 30 700 30 520 70 C330 115 170 150 0 130 Z" fill="#fce8f1"/>
    <path d="M30 160 C200 200 360 150 540 95 C720 42 900 50 1041 100 L1041 122 C900 72 720 68 545 120 C360 175 190 210 30 160 Z" fill="#eea4c8"/>
    <path d="M0 530 C120 490 260 505 420 540 C600 580 800 615 1041 545 L1041 630 L0 630 Z" fill="#85cae6"/>
    <path d="M0 552 C140 520 280 540 440 570 C620 605 820 640 1041 560 L1041 640 L0 640 Z" fill="#eea4c8"/>
    <path d="M0 570 C150 545 300 565 460 595 C640 628 840 655 1041 590 L1041 640 L0 640 Z" fill="#ffffff"/>
    <path d="M554 640 L554 602 C700 618 860 620 1041 590 L1041 640 Z" fill="#fce8f1"/>
    <path d="M0 1153 L520 1153 L510 1200 L0 1200 Z" fill="#85cae6"/>
    <path d="M530 1153 L1041 1153 L1041 1200 L520 1200 Z" fill="#eea4c8"/>
  </svg>

  <div class="abs right-panel"></div>

  <div class="abs brand">Sarah Lindqvist</div>
  <div class="abs tagline">Repair Your Relationship with Your Body and with Food</div>
  <div class="abs site-url">www.<b>sarahlindqvist</b>.com.au</div>

  <h1 class="abs title">The Quiet Bloom Gathering</h1>
  <div class="abs title-rule"></div>
  <p class="abs lead">It's time to make a commitment….<br>It's time for YOU, to SHOW UP for YOU…..</p>
  <p class="abs intro" style="top:334px">It's time to truly let go…….and finally heal, and find the peace that you so long for…You deserve to feel the freedom that comes with truly loving and accepting your body.</p>
  <p class="abs intro" style="top:410px">You deserve the freedom that comes with experiencing a deeper trusting connection with your body, where you feel safe, at home. Can you even imagine a whole day that you didn't hate your body, you didn't fight with food, and you felt peaceful and at home with your body? Can you love the part of you, that hates your body? You can't heal something you hate.</p>

  <div class="abs questions">
    <div>Are you truly ready to make the commitment?</div>
    <div class="big">How would it feel to be able to say,</div>
    <div>“I am free to love and accept my body”,</div>
    <div>and “I am free, connected and at peace to my body”?</div>
  </div>
  <p class="abs invite">I am inviting 10 women only into this six-week healing experience, as I personally know, that when we share our stories, it opens our hearts for other people to share their stories. It gives us the sense we are not alone in our journey's.</p>

  <div class="abs receive-band">The women that come on this six-week<br>journey will receive;</div>
  <ul class="abs benefits">
    <li class="gap"><svg width="14" height="14" viewBox="0 0 14 14"><rect x="1" y="1" width="12" height="12" fill="none" stroke="#333" stroke-width="1.4"/><path d="M3.5 7 L6 9.5 L11 3.5" fill="none" stroke="#333" stroke-width="1.6"/></svg>One 90mins one on one coaching session with me (which for the women that have attended the Friday circle previously, can be done before this healing circle begins);</li>
    <li class="narrow"><svg width="14" height="14" viewBox="0 0 14 14"><rect x="1" y="1" width="12" height="12" fill="none" stroke="#333" stroke-width="1.4"/><path d="M3.5 7 L6 9.5 L11 3.5" fill="none" stroke="#333" stroke-width="1.6"/></svg>Private Online Group to continue support outside of the circle</li>
    <li><svg width="14" height="14" viewBox="0 0 14 14"><rect x="1" y="1" width="12" height="12" fill="none" stroke="#333" stroke-width="1.4"/><path d="M3.5 7 L6 9.5 L11 3.5" fill="none" stroke="#333" stroke-width="1.6"/></svg>Homework outside of circle to support your healing</li>
    <li><svg width="14" height="14" viewBox="0 0 14 14"><rect x="1" y="1" width="12" height="12" fill="none" stroke="#333" stroke-width="1.4"/><path d="M3.5 7 L6 9.5 L11 3.5" fill="none" stroke="#333" stroke-width="1.6"/></svg>Journal and other small gifts weekly</li>
  </ul>

  <div class="abs portrait" role="img" aria-label="Portrait of Sarah Lindqvist in a pink jumper beside a leafy plant"></div>
  <div class="abs coach-name">Sarah Lindqvist</div>
  <div class="abs quote-mark" style="left:786px;top:734px">“</div>
  <p class="abs quote">It's time to show up for YOU, consistently, every week, and do the work, once and for all. No more games, no more half in on YOU….</p>
  <p class="abs quote-tail">You deserve better than a life contained in the mental<br>prison of body hatred</p>
  <div class="abs quote-mark" style="left:828px;top:888px">”</div>
  <p class="abs investment">The financial investment in YOU, is $XX for the six weeks. For the women that have attended the Friday night, Soft Strength Sister Circle, you will receive a discount of $100, taking the price to $XX.</p>
  <div class="abs ready">Are you ready?</div>
  <div class="abs social" aria-label="Social links"><span></span><span></span><span></span><span></span></div>

  <div class="abs call">Call us:<b>0400 555 217</b></div>
  <div class="abs email">
    <svg width="18" height="13" viewBox="0 0 18 13" aria-hidden="true"><rect x="0.5" y="0.5" width="17" height="12" fill="#222"/><path d="M1 1 L9 7.5 L17 1" fill="none" stroke="#eea4c8" stroke-width="1.3"/></svg>
    sarah@sarahlindqvist.com.au
  </div>
</main>
</body>
</html>
```